Brighten Your Compass - book web site

I need a web site for my book that is being published and will be available on Zorvel April 6th. It will have an email opt in which will then email the person a pdf report.
And it will have a bio page.
My logo, pic, book cover and bio details are attached below.

Target Market(s)

New life coaches that are looking to figure out their purpose and branding for their business

Industry/Entity Type

Life Coaching

Number of Pages Required

3 page

Font styles to use
Serif

Requirements
Must have
• The book cover, my logo, an opt in page, a bio page, my picture
• i would like the book in the header
• Needs to be chatterloop compliant
Should not have
• except for the logo, tranquil heart and soul will NOT be highlighted in the header

```html
<!DOCTYPE html>
<html lang="en">
<head>
<meta charset="utf-8">
<title>Brighten Your Compass – Marla Quenby</title>
<link rel="stylesheet" href="https://fonts.googleapis.com/css2?family=Lora:wght@400;700&family=Source+Serif+4:opsz,wght@8..60,400;8..60,600&family=Cinzel:wght@400;600&family=Libre+Caslon+Text:wght@400;700&display=swap">
<style>
  :root {
    --ink: #141414;
    --paper: #ffffff;
    --teal-light: #4fcfb0;
    --teal-deep: #1f9a8c;
    --cover-title: #5a2a78;
    --logo-orange: #c9561c;
    --field: rgba(255,255,255,0.42);
  }
  * { margin: 0; padding: 0; box-sizing: border-box; }
  html, body { width: 720px; height: 1200px; overflow: hidden; background: var(--paper); }
  body { position: relative; font-family: "Source Serif 4", Georgia, serif; color: var(--ink); }

  .site-header { position: absolute; left: 0; top: 0; width: 720px; height: 60px; background: var(--paper); }
  .brand { position: absolute; left: 78px; top: 27px; display: flex; align-items: center; gap: 4px;
    font-family: "Source Serif 4", serif; font-size: 9px; font-weight: 600; color: var(--logo-orange); letter-spacing: .3px; }
  .brand-dot { width: 8px; height: 8px; border-radius: 50%; background: var(--logo-orange); }
  .main-nav { position: absolute; top: 28px; left: 0; width: 720px; font-family: "Libre Caslon Text", serif; font-size: 12.5px; letter-spacing: .4px; }
  .main-nav a { position: absolute; color: var(--ink); text-decoration: none; white-space: nowrap; }
  .nav-who { left: 410px; }
  .nav-contact { left: 584px; }

  .hero { position: absolute; left: 0; top: 60px; width: 720px; height: 360px; overflow: hidden; }
  .hero-photo { position: absolute; inset: 0;
    background: linear-gradient(100deg, #5e4838 0%, #8f7763 35%, #a48d78 60%, #7d6654 100%); }
  .hero-title { position: absolute; left: 73px; top: 116px; width: 300px; font-family: "Lora", serif; font-weight: 700;
    font-size: 27px; line-height: 36px; color: #fff; }
  .hero-sub { position: absolute; left: 76px; top: 236px; font-family: "Lora", serif; font-weight: 700; font-size: 16px; color: #fff; }

  .book-cover { position: absolute; left: 440px; top: 3px; width: 238px; height: 355px; overflow: hidden;
    background: linear-gradient(160deg, var(--teal-light) 0%, #35b79d 55%, var(--teal-deep) 100%); }
  .cover-title { position: absolute; left: 0; top: 8px; width: 238px; text-align: center; font-family: "Cinzel", serif;
    font-size: 38px; line-height: 52px; color: var(--cover-title); }
  .cover-author { position: absolute; left: 0; bottom: 2px; width: 238px; text-align: center; font-size: 13px; color: #fff; }

  .bio { position: absolute; left: 0; top: 420px; width: 720px; height: 536px; }
  .section-title { position: absolute; left: 0; width: 756px; text-align: center; font-family: "Libre Caslon Text", serif;
    font-size: 27px; top: 32px; color: var(--ink); letter-spacing: .3px; }
  .bio-photo { position: absolute; left: 72px; top: 82px; width: 181px; height: 271px;
    background: linear-gradient(180deg, #b9b9b9 0%, #8a6a58 40%, #5c3e30 75%, #3a2a24 100%); }
  .bio-text { font-size: 12.3px; line-height: 18px; text-align: justify; hyphens: auto; }
  .bio-text p + p { margin-top: 13px; }
  .bio-side { position: absolute; left: 279px; top: 78px; width: 363px; }
  .bio-full { position: absolute; left: 78px; top: 371px; width: 564px; }

  .contact { position: absolute; left: 0; top: 956px; width: 720px; height: 244px; overflow: hidden; }
  .contact-photo { position: absolute; inset: 0;
    background: linear-gradient(100deg, #8b7664 0%, #b3a18f 40%, #c2b2a2 65%, #a08c79 100%); }
  .contact-title { position: absolute; left: 0; top: 16px; width: 732px; text-align: center; font-family: "Libre Caslon Text", serif;
    font-size: 27px; color: #fff; }
  .contact-sub { position: absolute; left: 0; top: 53px; width: 732px; text-align: center; font-family: "Lora", serif; font-size: 13.5px; color: #fff; }
  .optin label { position: absolute; font-family: "Lora", serif; font-size: 13.5px; color: #fff; }
  .optin input { position: absolute; height: 26px; border: 0; background: var(--field); }
  .lbl-first { left: 254px; top: 86px; } .in-first { left: 354px; top: 83px; width: 148px; }
  .lbl-last { left: 254px; top: 131px; } .in-last { left: 354px; top: 129px; width: 148px; }
  .lbl-email { left: 232px; top: 172px; } .in-email { left: 354px; top: 170px; width: 248px; }
  .send-btn { position: absolute; left: 282px; top: 206px; width: 147px; height: 25px; background: #fff;
    border: 1.5px solid #333; font-family: "Libre Caslon Text", serif; font-size: 16px; color: var(--ink); }
</style>
</head>
<body>
  <header class="site-header">
    <div class="brand"><span class="brand-dot"></span>TRANQUIL HEART AND SOUL</div>
    <nav class="main-nav">
      <a class="nav-who" href="#who">WHO IS MARLA</a>
      <a class="nav-contact" href="#contact">CONTACT</a>
    </nav>
  </header>

  <section class="hero">
    <div class="hero-photo" role="img" aria-label="Photo of a wooden desk with a vintage typewriter, old book, pine cone and notebook"></div>
    <h1 class="hero-title">Brighten Your Compass And Grow Your Business</h1>
    <p class="hero-sub">Available on Zorvel on April 6th</p>
    <div class="book-cover" role="img" aria-label="Book cover of Brighten Your Compass by Marla Quenby with its cover illustration">
      <div class="cover-title">BRIGHTEN<br>YOUR<br>COMPASS</div>
      <div class="cover-author">Marla Quenby</div>
    </div>
  </section>

  <section class="bio" id="who">
    <h2 class="section-title">WHO IS MARLA</h2>
    <div class="bio-photo" role="img" aria-label="Portrait photo of Marla Quenby"></div>
    <div class="bio-text bio-side">
      <p>Marla Quenby, founder of Tranquil Heart and Soul, helps new coaches and creative entrepreneurs find their inner voice so that they have the confidence to bring their authentic selves out into the world.</p>
      <p>Marla’s keen sense of what works is backed by a thorough education in psychology, health, nutrition, training and management. She’s a certified health counselor, having trained at the Institute for Whole Nourishment in New York (accredited by Eastbrook Teachers College).</p>
      <p>She holds a bachelor’s degree in psychology from Harborview University, giving her a deep understanding of the motivations behind food, career and lifestyle choices. She spent a decade in management with some of the most successful food businesses in the country.</p>
    </div>
    <div class="bio-text bio-full">
      <p>Marla has helped businesses achieve dramatic improvements in their organization and focus – in turn, making their businesses more profitable. Clients who seek Marla’s guidance are ready to get real and get wise, both in terms of health and business goals. She helps coaches quickly recognize easy to integrate strategies that will suit their work style to help eliminate the confusion on what to do next which in turn will boost their confidence and their bottom line.</p>
      <p>Marla is a classically trained culinary chef from Calloway &amp; Finch University and a certified raw foods chef, a certified yoga instructor, reiki master, a DeepRest facilitator, and a certified Business Coach for Wellness and Artistic Professionals.</p>
    </div>
  </section>

  <section class="contact" id="contact">
    <div class="contact-photo" role="img" aria-label="Soft-focus photo of a wooden desk with typewriter, book and notebook"></div>
    <h2 class="contact-title">CONTACT THE AUTHOR</h2>
    <p class="contact-sub">Email me and I will send a pdf report</p>
    <form class="optin">
      <label class="lbl-first" for="first">First Name</label><input class="in-first" id="first" type="text">
      <label class="lbl-last" for="last">Last Name</label><input class="in-last" id="last" type="text">
      <label class="lbl-email" for="email">Email Address</label><input class="in-email" id="email" type="email">
      <button class="send-btn" type="submit">SEND</button>
    </form>
  </section>
</body>
</html>
```